Coralbend Pastoral Traders Business Cards

We require business cards revamped with our logo. A few details we would like to use.

1. Round Edges
2. Our logo over the top of a wagyu cattle background photo on one side of the card

Other side of the card has the below details.

1. Person Name (First & Last)
2. Job Position
3. Mobile Number
4. Email Address
5. Website Address

Simple & Neat.

Target Market(s)

Sales

Industry/Entity Type

Agriculture

Contact Information for Business Card

CORALBEND PASTORAL TRADERS

Colors

Designer to choose colors to be used in the design.

Requirements
Must have
• Company Logo

```html
<!DOCTYPE html>
<html lang="en">
<head>
<meta charset="utf-8">
<title>Coralbend Pastoral Traders – Business Cards</title>
<link rel="stylesheet" href="https://fonts.googleapis.com/css2?family=Roboto:wght@400;700&display=swap">
<style>
  :root {
    --maroon: #6b1426;
    --maroon-soft: #8a3a4a;
    --paper: #ffffff;
    --stage: #2b2b2b;
    --photo-dark: #1c1512;
    --photo-wood: #4a2e1e;
    --photo-meat: #7a2a2e;
    --ink-light: #ffffff;
  }
  * { box-sizing: border-box; margin: 0; padding: 0; }
  html, body {
    width: 1200px; height: 875px; overflow: hidden;
    background: var(--stage);
    font-family: "Roboto", Arial, sans-serif;
  }
  .canvas {
    width: 1200px; height: 875px;
    display: flex; flex-direction: column; align-items: center; justify-content: center;
    gap: 40px;
  }
  .card {
    width: 660px; height: 377px;
    border-radius: 26px;
    overflow: hidden;
    position: relative;
    box-shadow: 0 14px 30px rgba(0,0,0,.45);
  }

  /* Front */
  .card-front { background: var(--photo-dark); }
  .card-front .photo {
    position: absolute; inset: 0;
    background:
      radial-gradient(ellipse at 55% 55%, var(--photo-meat) 0%, var(--photo-wood) 38%, var(--photo-dark) 78%);
  }
  .card-front .photo::after {
    content: ""; position: absolute; inset: 0;
    background: rgba(0,0,0,.35);
  }
  .front-brand {
    position: absolute; inset: 0;
    display: flex; align-items: center; justify-content: center; gap: 16px;
    color: var(--ink-light);
  }
  .front-brand .mark {
    width: 26px; height: 26px; border-radius: 50%;
    background: var(--ink-light);
  }
  .front-brand .name {
    font-size: 32px; font-weight: 700; letter-spacing: 2px;
  }

  /* Back */
  .card-back { background: var(--paper); color: var(--maroon); }
  .back-brand {
    position: absolute; top: 44px; right: 48px;
    display: flex; align-items: center; gap: 10px;
  }
  .back-brand .mark {
    width: 16px; height: 16px; border-radius: 50%; background: var(--maroon);
  }
  .back-brand .name {
    font-size: 17px; font-weight: 700; letter-spacing: 1.2px;
  }
  .header-rule {
    position: absolute; top: 92px; left: 250px; right: 48px;
    height: 1.5px; background: var(--maroon);
  }
  .person {
    position: absolute; left: 44px; top: 170px;
  }
  .person-name {
    font-size: 34px; font-weight: 700; letter-spacing: .5px;
  }
  .person-role {
    font-size: 17px; margin-top: 4px; color: var(--maroon);
  }
  .person-rule {
    width: 300px; height: 1.5px; background: var(--maroon); margin: 16px 0 14px;
  }
  .contact-list { list-style: none; }
  .contact-list li {
    display: flex; align-items: center; gap: 12px;
    font-size: 15px; line-height: 1; margin-bottom: 11px;
  }
  .contact-list svg { width: 15px; height: 15px; fill: var(--maroon); flex: none; }
</style>
</head>
<body>
<main class="canvas">

  <section class="card card-front">
    <div class="photo" role="img" aria-label="Wagyu beef cuts on a wooden board with herbs and spices on a dark table"></div>
    <div class="front-brand">
      <span class="mark"></span>
      <span class="name">CORALBEND PASTORAL TRADERS</span>
    </div>
  </section>

  <section class="card card-back">
    <div class="back-brand">
      <span class="mark"></span>
      <span class="name">CORALBEND PASTORAL TRADERS</span>
    </div>
    <div class="header-rule"></div>

    <div class="person">
      <h1 class="person-name">LIAM HARROW</h1>
      <p class="person-role">Managing Director</p>
      <div class="person-rule"></div>
      <ul class="contact-list">
        <li>
          <svg viewBox="0 0 16 16" aria-hidden="true"><path d="M4 1h8a1 1 0 0 1 1 1v12a1 1 0 0 1-1 1H4a1 1 0 0 1-1-1V2a1 1 0 0 1 1-1zm1 2v9h6V3zm3 10.2a.8.8 0 1 0 0-1.6.8.8 0 0 0 0 1.6z"/></svg>
          <span>07 5550 1482</span>
        </li>
        <li>
          <svg viewBox="0 0 16 16" aria-hidden="true"><path d="M1 3h14v10H1zm1.5 1.2V5l5.5 4 5.5-4v-.8L8 8.2z"/></svg>
          <span>info@coralbendpastoral.com</span>
        </li>
        <li>
          <svg viewBox="0 0 16 16" aria-hidden="true"><path d="M8 1a7 7 0 1 0 0 14A7 7 0 0 0 8 1zm0 1.5c.8 0 1.7 1.6 2 4H6c.3-2.4 1.2-4 2-4zM2.6 7.5h2.3c0 .4-.1.7-.1 1s0 .7.1 1H2.6a5.6 5.6 0 0 1 0-2zm3.4 2h4c-.3 2.4-1.2 4-2 4s-1.7-1.6-2-4zm5.1 0c0-.3.1-.7.1-1s0-.6-.1-1h2.3a5.6 5.6 0 0 1 0 2z"/></svg>
          <span>coralbendpastoral.com</span>
        </li>
      </ul>
    </div>
  </section>

</main>
</body>
</html>
```